Stylish Business Cards Wanted

- DOUBLE SIDED Design Required -

High end, edgy cards for a corporate and personal stylist. Must include logo,
Name: Belinda Forsey
Title: Director and Stylist
telephone : +61 8 8217 4592
email: belinda@thegarbledger.example
website: thegarbledger.example
Tag: Corporate Workwear & Uniform Specialist | Personal Stylist
Would like nice icons for telephone, email, website

Target Market(s)

Businesses wanting stylish uniforms, people wanting stylish wardrobes

Industry/Entity Type

Corporate Workwear Stylist

Contact Information for Business Card

I would like black, white and gold foiling incorporated in the design - possibly a touch of the other colours on my branding guide attached Name: Belinda Forsey Title: Director and Stylist telephone : +61 8 8217 4592 email: belinda@thegarbledger.example website: thegarbledger.example Tag: Corporate Workwear & Uniform Specialist | Personal Stylist Would like nice icons for telephone, email, website

Font styles to use
Other font styles liked:
• Raleway

Colors

Designer to choose colors to be used in the design.

Requirements
Must have
• Gold foil accents

```html
<!DOCTYPE html>
<html lang="en">
<head>
<meta charset="utf-8">
<title>The Garb Ledger – Business Cards</title>
<link rel="stylesheet" href="https://fonts.googleapis.com/css2?family=Arimo:wght@400;500&family=Oswald:wght@500&display=swap">
<style>
  :root {
    --backdrop: #2b2b2b;
    --card: #171717;
    --gold: #e8bf52;
    --white: #f1f1f1;
    --soft-white: #d9d9d9;
    --divider: #3a3a3a;
  }
  * { box-sizing: border-box; margin: 0; padding: 0; }
  html, body { width: 1200px; height: 900px; overflow: hidden; }
  body {
    background: var(--backdrop);
    font-family: "Arimo", Arial, sans-serif;
    color: var(--white);
    display: flex;
    flex-direction: column;
    align-items: center;
    justify-content: center;
    gap: 48px;
  }
  .card {
    position: relative;
    width: 630px;
    height: 360px;
    background: var(--card);
    box-shadow: 0 10px 30px rgba(0,0,0,.45);
    overflow: hidden;
  }
  .card__band {
    position: absolute;
    left: 0; right: 0; bottom: 0;
    height: 7px;
    background: var(--gold);
  }

  /* Front */
  .card--front .brand {
    position: absolute;
    top: 118px;
    left: 0; right: 0;
    display: flex;
    align-items: center;
    justify-content: center;
    gap: 14px;
  }
  .brand__dot {
    width: 14px; height: 14px;
    border-radius: 50%;
    background: var(--gold);
  }
  .brand__name {
    font-weight: 500;
    font-size: 46px;
    color: var(--white);
    letter-spacing: 1px;
  }
  .card--front .tagline {
    position: absolute;
    bottom: 34px;
    left: 0; right: 0;
    text-align: center;
    font-size: 17px;
    color: var(--white);
    letter-spacing: .3px;
  }
  .tagline__sep {
    display: inline-block;
    width: 6px; height: 6px;
    border-radius: 50%;
    background: var(--gold);
    margin: 0 12px;
    vertical-align: middle;
  }

  /* Back */
  .person {
    position: absolute;
    top: 128px;
    left: 50px;
    width: 270px;
    text-align: right;
  }
  .person__name {
    font-family: "Oswald", "Arial Narrow", sans-serif;
    font-weight: 500;
    font-size: 38px;
    line-height: 1;
    color: var(--gold);
    text-transform: uppercase;
  }
  .person__title {
    font-size: 17px;
    color: var(--soft-white);
    margin-top: 6px;
  }
  .divider {
    position: absolute;
    top: 120px;
    left: 340px;
    width: 1px;
    height: 80px;
    background: var(--divider);
  }
  .contacts {
    position: absolute;
    top: 124px;
    left: 362px;
    list-style: none;
  }
  .contacts li {
    display: flex;
    align-items: center;
    gap: 10px;
    font-size: 16px;
    color: var(--white);
    line-height: 25px;
  }
  .contacts svg {
    width: 15px; height: 15px;
    flex: none;
    fill: none;
    stroke: var(--gold);
    stroke-width: 1.8;
  }
</style>
</head>
<body>

  <section class="card card--front" aria-label="Business card front">
    <div class="brand">
      <span class="brand__dot"></span>
      <span class="brand__name">The Garb Ledger</span>
    </div>
    <p class="tagline">Corporate Workwear &amp; Uniform Specialist<span class="tagline__sep"></span>Personal Stylist</p>
    <div class="card__band"></div>
  </section>

  <section class="card card--back" aria-label="Business card back">
    <div class="person">
      <h1 class="person__name">Belinda Forsey</h1>
      <p class="person__title">Director and Stylist</p>
    </div>
    <div class="divider"></div>
    <ul class="contacts">
      <li>
        <svg viewBox="0 0 24 24" aria-hidden="true"><path d="M5 3h4l2 5-2.5 1.5a11 11 0 0 0 6 6L16 13l5 2v4a2 2 0 0 1-2 2A17 17 0 0 1 3 5a2 2 0 0 1 2-2z"/></svg>
        +61 8 8217 4592
      </li>
      <li>
        <svg viewBox="0 0 24 24" aria-hidden="true"><rect x="2.5" y="5" width="19" height="14"/><path d="M2.5 5l9.5 8 9.5-8"/></svg>
        belinda@thegarbledger.example
      </li>
      <li>
        <svg viewBox="0 0 24 24" aria-hidden="true"><circle cx="12" cy="12" r="9.5"/><path d="M2.5 12h19M12 2.5c3 3 3 16 0 19M12 2.5c-3 3-3 16 0 19"/></svg>
        thegarbledger.example
      </li>
    </ul>
    <div class="card__band"></div>
  </section>

</body>
</html>
```